Business Card Design Project

Business Card
We are rebranding with a new logo
Industry/Entity Type
Business
Contact Information for Business Card
Dennis Marlow +61 427581962 dennis@qovo.com.au P.O. Box 872 Kelvindale QLD 4309
Requirements
Must have
- Logo

```html
<!DOCTYPE html>
<html lang="en">
<head>
<meta charset="UTF-8">
<title>Qovo International — Business Card</title>
<link href="https://fonts.googleapis.com/css2?family=Montserrat:wght@400;600;700&display=swap" rel="stylesheet">
<style>
  :root {
    --canvas-bg: #e2e4e6;
    --card-blue: #179fd8;
    --card-navy: #0b4a6f;
    --card-white: #ffffff;
    --brand-blue: #1a86c4;
    --text-light: #ffffff;
  }
  * { margin: 0; padding: 0; box-sizing: border-box; }
  html, body {
    width: 1200px; height: 1200px; overflow: hidden;
    background: var(--canvas-bg);
    font-family: "Montserrat", Arial, sans-serif;
  }
  .business-card {
    position: absolute;
    left: 350px; top: 185px;
    width: 500px; height: 830px;
    background: var(--card-blue);
    overflow: hidden;
    box-shadow: 0 6px 18px rgba(0,0,0,0.12);
  }
  .card-name {
    position: absolute; top: 130px; left: 0; width: 100%;
    text-align: center;
    font-weight: 700; font-size: 42px; letter-spacing: 0.5px;
    color: var(--card-navy);
    text-transform: uppercase;
  }
  .contact-list {
    position: absolute; top: 262px; left: 62px;
    list-style: none;
    color: var(--text-light);
    font-size: 20px; line-height: 34px;
  }
  .contact-list li { display: flex; align-items: center; gap: 12px; }
  .contact-icon { width: 18px; height: 18px; flex: none; fill: var(--text-light); }
  .card-base { position: absolute; left: 0; top: 0; width: 500px; height: 830px; }
  .brand {
    position: absolute; top: 660px; left: 0; width: 100%;
    display: flex; justify-content: center; align-items: center; gap: 14px;
  }
  .brand-dot { width: 22px; height: 22px; border-radius: 50%; background: var(--brand-blue); }
  .brand-name {
    font-weight: 700; font-size: 34px; letter-spacing: 1px;
    color: var(--brand-blue);
  }
</style>
</head>
<body>
  <div class="business-card">
    <svg class="card-base" viewBox="0 0 500 830" aria-hidden="true">
      <path d="M0 575 Q 230 480 500 440 L500 830 L0 830 Z" fill="var(--card-white)"/>
      <path d="M0 575 Q 230 480 500 440" fill="none" stroke="var(--card-navy)" stroke-width="10"/>
    </svg>

    <h1 class="card-name">Dennis Marlow</h1>

    <ul class="contact-list">
      <li>
        <svg class="contact-icon" viewBox="0 0 24 24"><path d="M2 9c0-3 5-5 10-5s10 2 10 5v2h-5V8.5c-1.5-.6-3.2-.9-5-.9s-3.5.3-5 .9V11H2zm4 4h12l2 7H4zm6 1.5a2.5 2.5 0 1 0 0 5 2.5 2.5 0 0 0 0-5z"/></svg>
        <span>+61 427581962</span>
      </li>
      <li>
        <svg class="contact-icon" viewBox="0 0 24 24"><path d="M2 5h20v14H2zm2 2v.5l8 6 8-6V7zm0 3v7h16v-7l-8 6z"/></svg>
        <span>dennis@qovo.com.au</span>
      </li>
      <li>
        <svg class="contact-icon" viewBox="0 0 24 24"><path d="M12 2a7 7 0 0 0-7 7c0 5 7 13 7 13s7-8 7-13a7 7 0 0 0-7-7zm0 4a3 3 0 1 1 0 6 3 3 0 0 1 0-6z"/></svg>
        <span>P.O. Box 872 Kelvindale QLD 4309</span>
      </li>
    </ul>

    <div class="brand">
      <span class="brand-dot"></span>
      <span class="brand-name">Qovo International</span>
    </div>
  </div>
</body>
</html>
```